Powepoint Templates From Logo

Hello,

I am looking for a template for PowerPoint presentations for a new company selling LED's. The PowerPoint should keep the look and feel of our newly designed website ( which is still under development ) http://brivoxa.com/development/

I have attached our Logo which should be included in this template.
This PowerPoint will be used towards client during demonstrations and for internal use.

This template should be complete with fonts and colors of the text for both headlines and bullets/normal text.

I guess the easiest way for me to determine what I like is to see some dummy info/text on the submitted designs.

Thanks

Industry/Entity Type

It Company

Requirements
Must have
• Should include our logo

```html
<!DOCTYPE html>
<html lang="en">
<head>
<meta charset="utf-8">
<title>Brivoxa Presentation Template</title>
<link rel="stylesheet" href="https://fonts.googleapis.com/css2?family=Arimo:wght@400;700&display=swap">
<style>
  :root {
    --green-dark: #5d8a0c;
    --green-mid: #8ab81f;
    --green-light: #c6e33f;
    --slide-top: #e4e7ea;
    --slide-bottom: #ffffff;
    --text-dark: #1a1a1a;
    --text-grey: #5a5a5a;
    --heading-grey: #9a9a9a;
    --frame: #8db83a;
    --white: #ffffff;
  }
  * { margin: 0; padding: 0; box-sizing: border-box; }
  html, body {
    width: 1200px; height: 1020px; overflow: hidden;
    background: var(--white);
    font-family: "Arimo", Arial, sans-serif;
  }
  .canvas { position: relative; width: 1200px; height: 1020px; }

  .slide {
    position: absolute; width: 578px; height: 378px; overflow: hidden;
    background: linear-gradient(180deg, var(--slide-top) 0%, var(--slide-bottom) 55%);
    border: 1px solid #9aa38c;
  }
  .slide--title   { left: 14px;  top: 116px; }
  .slide--why     { left: 599px; top: 116px; }
  .slide--bulb    { left: 14px;  top: 504px; }
  .slide--benefit { left: 602px; top: 504px; }

  .band-top {
    position: absolute; left: 0; top: 0; width: 100%;
    background: linear-gradient(90deg, var(--green-dark) 0%, var(--green-mid) 60%, var(--green-light) 100%);
  }
  .band-top--thin { height: 29px; }
  .band-top--header { height: 67px; }
  .band-bottom {
    position: absolute; left: 0; bottom: 0; width: 100%; height: 14px;
    background: linear-gradient(90deg, var(--green-light) 0%, var(--green-mid) 40%, var(--green-dark) 100%);
  }

  .slide-title {
    position: absolute; left: 94px; top: 19px;
    color: var(--white); font-size: 26px; font-weight: 400; letter-spacing: -0.5px;
  }
  .slide-title strong { font-weight: 700; }
  .slide-url {
    position: absolute; right: 22px; top: 28px;
    color: var(--white); font-size: 14px; font-weight: 700; letter-spacing: 2.4px;
  }

  .brand { position: absolute; display: flex; align-items: center; gap: 8px; }
  .brand-dot { border-radius: 50%; background: var(--green-mid); }
  .brand-name { font-weight: 700; color: var(--text-grey); }
  .brand--large { left: 0; right: 0; top: 40px; justify-content: center; gap: 12px; }
  .brand--large .brand-dot { width: 60px; height: 60px; }
  .brand--large .brand-name { font-size: 44px; }
  .brand--small { left: 434px; top: 310px; }
  .brand--small .brand-dot { width: 36px; height: 36px; }
  .brand--small .brand-name { font-size: 24px; }

  .hero-photo {
    position: absolute; left: 131px; top: 175px; width: 319px; height: 108px;
    border-radius: 8px; border: 1px solid #8e9b6a;
    background: linear-gradient(180deg, #d7ea6a 0%, #a9cc2e 100%);
  }
  .title-url {
    position: absolute; left: 0; right: 0; top: 320px; text-align: center;
    font-size: 15px; font-weight: 700; letter-spacing: 3px; color: var(--text-grey);
  }

  .body-copy {
    position: absolute; left: 94px; top: 98px; width: 402px;
    font-size: 13.4px; font-weight: 700; line-height: 18.6px;
    color: var(--text-dark); text-align: justify;
  }

  .section-heading {
    position: absolute; left: 0; right: 0; top: 80px; text-align: center;
    font-size: 22px; font-weight: 700; color: var(--heading-grey);
  }
  .product-grid {
    position: absolute; left: 96px; top: 119px;
    display: grid; grid-template-columns: repeat(4, 94px); grid-auto-rows: 79px;
    column-gap: 2px; row-gap: 5px;
  }
  .product-tile { border: 1.5px solid var(--frame); }
  .product-tile--1 { background: linear-gradient(135deg, #dfe6ec, #6f8fb6); }
  .product-tile--2 { background: radial-gradient(circle, #eaf3ff 0%, #3c5fa8 45%, #08122e 100%); }
  .product-tile--3 { background: radial-gradient(circle at 40% 40%, #d25fc3 0%, #3a1037 70%, #0c0710 100%); }
  .product-tile--4 { background: linear-gradient(135deg, #f1f0ea, #b49a5e); }
  .product-tile--5 { background: linear-gradient(180deg, #e8e8e8 0%, #b23a3a 55%, #2d7c46 100%); }
  .product-tile--6 { background: linear-gradient(135deg, #f4f4f2, #a68d66); }
  .product-tile--7 { background: linear-gradient(135deg, #d9d4c6, #8a7f68); }
  .product-tile--8 { background: linear-gradient(135deg, #ffffff, #cfd2d4); }

  .feature {
    position: absolute; left: 98px; top: 98px; width: 456px;
    font-size: 10.9px; font-weight: 700; line-height: 14.6px;
    color: var(--text-dark); text-align: justify;
  }
  .feature-photo {
    float: left; width: 215px; height: 138px; margin: 0 14px 2px 0;
    border: 1.5px solid var(--frame);
    background: linear-gradient(180deg, #b9d3e6 0%, #e6eef2 55%, #8fae4b 100%);
  }
  .brand--footer { left: 436px; top: 296px; }
  .footer-url {
    position: absolute; left: 412px; top: 338px;
    font-size: 11px; font-weight: 700; letter-spacing: 1.5px; color: var(--green-mid);
  }
</style>
</head>
<body>
<main class="canvas">

  <section class="slide slide--title">
    <div class="band-top band-top--thin"></div>
    <div class="brand brand--large">
      <span class="brand-dot"></span>
      <span class="brand-name">Brivoxa</span>
    </div>
    <div class="hero-photo" role="img" aria-label="Row of coloured LED diodes in orange, yellow, green and red"></div>
    <p class="title-url">www.brivoxa.com</p>
    <div class="band-bottom"></div>
  </section>

  <section class="slide slide--why">
    <div class="band-top band-top--header"></div>
    <h2 class="slide-title">Why <strong>LED?</strong></h2>
    <p class="slide-url">www.brivoxa.com</p>
    <p class="body-copy">It is a long established fact that a reader will be distracted by the readable content of a page when looking at its layout. The point of using Lorem Ipsum is that it has a more-or-less normal distribution of letters, as opposed to using ‘Content here, content here’, making it look like readable English. Many desktop publishing packages and web page editors now use Lorem Ipsum as their default model text, and a search for ‘lorem ipsum’ will uncover many web sites still in their infancy. Various versions have evolved over the years, sometimes by accident, sometimes on purpose (injected humour and the like).</p>
    <div class="brand brand--small">
      <span class="brand-dot"></span>
      <span class="brand-name">Brivoxa</span>
    </div>
    <div class="band-bottom"></div>
  </section>

  <section class="slide slide--bulb">
    <div class="band-top band-top--header"></div>
    <h2 class="slide-title"><strong>LED</strong> Bulb</h2>
    <p class="slide-url">www.brivoxa.com</p>
    <h3 class="section-heading">All Products</h3>
    <div class="product-grid">
      <div class="product-tile product-tile--1" role="img" aria-label="Candle-shaped coloured bulbs"></div>
      <div class="product-tile product-tile--2" role="img" aria-label="Glowing round LED light"></div>
      <div class="product-tile product-tile--3" role="img" aria-label="Pink spotlight beam"></div>
      <div class="product-tile product-tile--4" role="img" aria-label="Row of LED spot bulbs"></div>
      <div class="product-tile product-tile--5" role="img" aria-label="Rows of coloured festoon bulbs"></div>
      <div class="product-tile product-tile--6" role="img" aria-label="Bulb socket fitting"></div>
      <div class="product-tile product-tile--7" role="img" aria-label="Ceramic lamp holder"></div>
      <div class="product-tile product-tile--8" role="img" aria-label="White frosted LED bulb"></div>
    </div>
    <div class="brand brand--small">
      <span class="brand-dot"></span>
      <span class="brand-name">Brivoxa</span>
    </div>
    <div class="band-bottom"></div>
  </section>

  <section class="slide slide--benefit">
    <div class="band-top band-top--header"></div>
    <h2 class="slide-title">Advantage of <strong>LED</strong></h2>
    <p class="slide-url">www.brivoxa.com</p>
    <div class="feature">
      <div class="feature-photo" role="img" aria-label="Open hands holding a small young tree against a blue sky"></div>
      <p>It is a long established fact that a reader will be distracted by the readable content of a page when looking at its layout. The point of using Lorem Ipsum is that it has a more-or-less normal distribution of letters, as opposed to using ‘Content here, content here’, making it look like readable English. Many desktop publishing packages and web page editors now use Lorem Ipsum as their default model text, and a search for ‘lorem ipsum’ will uncover many web sites still in their infancy. Various versions have evolved over the years, sometimes by accident, sometimes on purpose (injected humour and the like).</p>
    </div>
    <div class="brand brand--small brand--footer">
      <span class="brand-dot"></span>
      <span class="brand-name">Brivoxa</span>
    </div>
    <p class="footer-url">www.brivoxa.com</p>
    <div class="band-bottom"></div>
  </section>

</main>
</body>
</html>
```